Professional
Miriam T. Hollisby, Esq.
Attorney at Law
Hollisby & Dunmore, LLC
4127 Fernhaven Court
Atlanta, Georgia 30305
mhollisby@hd-counsel.net
www.hd-counsel.net
I may want to include a photo. I have uploaded a photo. I'd like to see if it looks appropriate, if not, we'll go without a photo. Please use the logo that is uploaded
Please use the logo that is uploaded in some way. Possibly the corresponding black background with whitel letters for the back.
Photo to possibly be included on busines cards

```html
<!DOCTYPE html>
<html lang="en">
<head>
<meta charset="UTF-8">
<title>Hollisby &amp; Dunmore, LLC — Business Card</title>
<link href="https://fonts.googleapis.com/css2?family=Arimo:wght@400;700&display=swap" rel="stylesheet">
<style>
  :root {
    --canvas: #ecebe8;
    --card-white: #ffffff;
    --card-shade: #e4e4e4;
    --card-black: #0b0b0b;
    --ink: #222222;
    --ink-soft: #3a3a3a;
    --accent-red: #c8102e;
    --rule: #8a8a8a;
    --faint-mark: #1c1c1c;
    --on-dark: #f2f2f2;
  }
  * { margin: 0; padding: 0; box-sizing: border-box; }
  html, body {
    width: 1200px;
    height: 1037px;
    overflow: hidden;
    background: var(--canvas);
    font-family: "Arimo", Arial, sans-serif;
  }
  .stage { position: relative; width: 1200px; height: 1037px; }

  .card {
    position: absolute;
    width: 720px;
    height: 412px;
    box-shadow: 0 6px 18px rgba(0,0,0,0.18);
  }

  /* Front */
  .card-front {
    left: 100px;
    top: 120px;
    background: linear-gradient(180deg, var(--card-white) 0%, var(--card-white) 55%, var(--card-shade) 100%);
  }
  .brand-block {
    position: absolute;
    left: 0;
    top: 0;
    width: 330px;
    height: 100%;
    display: flex;
    align-items: center;
    justify-content: center;
    gap: 10px;
  }
  .brand-dot {
    width: 14px;
    height: 14px;
    border-radius: 50%;
    background: var(--accent-red);
    flex: none;
  }
  .brand-name {
    font-weight: 700;
    font-size: 22px;
    color: var(--ink);
    letter-spacing: 0.3px;
  }
  .divider {
    position: absolute;
    left: 330px;
    top: 78px;
    width: 1px;
    height: 255px;
    background: var(--rule);
  }
  .contact {
    position: absolute;
    left: 362px;
    top: 80px;
    color: var(--ink);
    font-size: 15.5px;
    line-height: 1.32;
  }
  .contact .person {
    font-size: 18px;
  }
  .contact .person-name {
    color: var(--accent-red);
    font-weight: 700;
  }
  .contact .title { margin-bottom: 22px; }
  .contact .row { display: flex; }
  .contact .label { width: 52px; }
  .contact .web {
    margin-top: 20px;
    color: var(--accent-red);
  }

  /* Back */
  .card-back {
    left: 380px;
    top: 520px;
    background: var(--card-black);
    overflow: hidden;
  }
  .back-watermark {
    position: absolute;
    left: 30px;
    top: 40px;
    font-weight: 700;
    font-size: 150px;
    line-height: 1;
    color: var(--faint-mark);
    white-space: nowrap;
  }
  .back-brand {
    position: absolute;
    right: 36px;
    bottom: 40px;
    text-align: right;
    color: var(--on-dark);
  }
  .back-brand .brand-name {
    color: var(--on-dark);
    font-size: 20px;
    display: block;
    margin-bottom: 10px;
  }
  .back-brand .web {
    font-size: 13px;
  }
</style>
</head>
<body>
<main class="stage">

  <section class="card card-front" aria-label="Business card front">
    <div class="brand-block">
      <span class="brand-dot"></span>
      <span class="brand-name">Hollisby &amp; Dunmore, LLC</span>
    </div>
    <div class="divider"></div>
    <div class="contact">
      <div class="person"><span class="person-name">Miriam T. Hollisby</span>, Esq.</div>
      <div class="title">Attorney at Law</div>
      <div>Hollisby &amp; Dunmore, LLC</div>
      <div>4127 Fernhaven Court</div>
      <div>Atlanta, Georgia 30305</div>
      <div class="row"><span class="label">Phone:</span><span>404-555-0182</span></div>
      <div class="row"><span class="label">Fax:</span><span>404-555-0183</span></div>
      <div class="row"><span class="label">Email:</span><span>mhollisby@hd-counsel.net</span></div>
      <div class="web">www.hd-counsel.net</div>
    </div>
  </section>

  <section class="card card-back" aria-label="Business card back">
    <div class="back-watermark">Hollisby</div>
    <div class="back-brand">
      <span class="brand-name">Hollisby &amp; Dunmore, LLC</span>
      <span class="web">www.hd-counsel.net</span>
    </div>
  </section>

</main>
</body>
</html>
```